New Optometry Practice needs a Business Card

Need a business card for an Optometry practice called 'Marlow Vista Eyecare'. I would like to use designs that are friendly, fun and professional. Looking to incorporate glasses (see uploaded image). Not interested in design with an 'eye' in logo. Like green, blue, white as color choices..but open to your ideas. Back of card will be an appointment card as well as provide address, phone and email information.

Industry/Entity Type

Business

Contact Information for Business Card

Marlow Vista Eyecare
Dr. Petra Lindqvist, Optometrist (or O.D.)
4172 S Corbell Ave Wenatchee, WA 98736
PMarlowvistaeyecare.example

Colors
acd036
33b8a4
f68d4e
cfeae6
fee18a
cadf82

Requirements
Must have
• Appointment card on back with date/time of return for next exam

```html
<!DOCTYPE html>
<html lang="en">
<head>
<meta charset="utf-8">
<title>Marlow Vista Eyecare – Business Card</title>
<link href="https://fonts.googleapis.com/css2?family=Arimo:wght@400&family=Open+Sans:wght@400&family=Karla:wght@400&display=swap" rel="stylesheet">
<style>
  :root {
    --canvas-bg: #e9e9e7;
    --card-orange: #e57718;
    --card-white: #ffffff;
    --frame-teal: #00ab8e;
    --ink-light: #ffffff;
    --ink-orange: #e57718;
  }
  * { margin: 0; padding: 0; box-sizing: border-box; }
  html, body {
    width: 1200px;
    height: 1200px;
    overflow: hidden;
    background: var(--canvas-bg);
  }
  .canvas {
    position: relative;
    width: 1200px;
    height: 1200px;
  }
  .card {
    position: absolute;
    left: 160px;
    width: 880px;
    height: 500px;
    overflow: hidden;
    box-shadow: 0 6px 18px rgba(0,0,0,0.18);
  }
  .card--front { top: 70px; background: var(--card-orange); }
  .card--back  { top: 630px; background: var(--card-white); }

  .doctor {
    position: absolute;
    top: 110px;
    right: 110px;
    text-align: right;
    color: var(--ink-light);
  }
  .doctor__name {
    font-family: "Arimo", Arial, sans-serif;
    font-size: 34px;
    line-height: 1.1;
  }
  .doctor__title {
    font-family: "Open Sans", sans-serif;
    font-size: 21px;
    line-height: 1.3;
  }
  .practice-name {
    position: absolute;
    left: 110px;
    bottom: 58px;
    font-family: "Arimo", Arial, sans-serif;
    font-size: 40px;
    line-height: 1.1;
    white-space: nowrap;
    color: var(--ink-light);
  }
  .frame-art {
    position: absolute;
    display: block;
  }
  .card--front .frame-art { right: -10px; top: 225px; width: 300px; height: 165px; }
  .card--back .frame-art  { left: -10px; top: 270px; width: 330px; height: 185px; }

  .contact {
    position: absolute;
    top: 105px;
    right: 70px;
    text-align: right;
    font-family: "Karla", sans-serif;
    font-size: 24px;
    line-height: 1.4;
    letter-spacing: 0.5px;
    color: var(--ink-orange);
  }
  .appointment {
    position: absolute;
    left: 590px;
    top: 395px;
    font-family: "Karla", sans-serif;
    font-size: 24px;
    color: var(--ink-orange);
    letter-spacing: 0.5px;
  }
  .appointment__field { height: 56px; }
</style>
</head>
<body>
<main class="canvas">
  <section class="card card--front">
    <div class="doctor">
      <p class="doctor__name">Dr. Petra Lindqvist</p>
      <p class="doctor__title">optometrist (or O.D.)</p>
    </div>
    <svg class="frame-art" role="img" aria-label="Teal glasses frame illustration" viewBox="0 0 300 165">
      <rect x="0" y="0" width="300" height="165" rx="70" fill="var(--frame-teal)"/>
    </svg>
    <p class="practice-name">Marlow Vista Eyecare</p>
  </section>

  <section class="card card--back">
    <div class="contact">
      <p>4172 S Corbell Ave Wenatchee, WA 98736</p>
      <p>PMarlowvistaeyecare.example</p>
    </div>
    <svg class="frame-art" role="img" aria-label="Teal glasses frame illustration" viewBox="0 0 330 185">
      <rect x="0" y="0" width="330" height="185" rx="70" fill="var(--frame-teal)"/>
    </svg>
    <div class="appointment">
      <p class="appointment__field">Date</p>
      <p class="appointment__field">Time</p>
    </div>
  </section>
</main>
</body>
</html>
```